harbor institute of business and technology web site

I need web site for the institute which focus on business courses and computer course it is also for vocation train for employment It is also carear development and advancement .It should have links to online study resource which free
Industry/Entity Type
Business
Number of Pages Required
1 page
Look and feel
Each slider illustrates characteristics of the customer's brand and the style your logo design should communicate.

```html
<!DOCTYPE html>
<html lang="en">
<head>
<meta charset="utf-8">
<title>Harbor Institute of Business and Technology</title>
<link href="https://fonts.googleapis.com/css2?family=Open+Sans:wght@400;600;700&display=swap" rel="stylesheet">
<style>
:root{
  --orange:#f0921e;
  --orange-dark:#d9761a;
  --ink:#222;
  --dark:#2a2a2a;
  --darker:#1c1c1c;
  --panel:#3a3a3a;
  --grey:#e4e4e4;
  --line:#cfcfcf;
  --card:#d6e7f3;
  --white:#fff;
  --text:#333;
}
*{box-sizing:border-box;margin:0;padding:0}
html,body{width:1200px;height:4136px;overflow:hidden}
body{font-family:"Open Sans",Arial,sans-serif;color:var(--text);background:#f4f4f4;position:relative}
.header{position:absolute;left:0;top:0;width:1200px;height:208px;background:linear-gradient(#ededed,#dcdcdc)}
.brand{position:absolute;left:56px;top:30px;display:flex;align-items:center;gap:12px}
.brand-mark{width:44px;height:44px;background:#1f4f9a}
.brand-name{font-size:20px;font-weight:700;color:#1f4f9a;width:220px;line-height:1.2}
.user-links{position:absolute;right:230px;top:40px;font-size:18px;color:#444;display:flex;gap:26px}
.search{position:absolute;right:56px;top:112px;display:flex}
.search-field{width:180px;height:44px;background:#fff;border:1px solid #bbb;font-size:16px;color:#888;padding:10px 14px}
.search-btn{width:52px;height:44px;background:var(--panel)}
.nav{position:absolute;left:0;top:208px;width:1200px;height:52px;background:var(--orange);display:flex}
.nav a{flex:1;color:#fff;text-decoration:none;font-size:21px;font-weight:600;display:flex;align-items:center;justify-content:center;border-right:1px solid var(--orange-dark)}
.nav a.active{background:var(--dark);flex:0.8}
.hero{position:absolute;left:0;top:260px;width:1200px;height:462px;background:linear-gradient(120deg,#6d7680,#b9c2c8 45%,#4d4a48)}
.sidebar{position:absolute;left:48px;top:728px;width:392px}
.login{background:var(--dark);height:430px;padding:22px 24px;color:#ddd}
.login h3{font-size:15px;font-weight:600;color:#fff;background:var(--orange);padding:4px 10px;display:inline-block;margin-bottom:24px}
.field{height:46px;background:#fff;margin-bottom:16px;font-size:17px;color:#888;padding:11px 14px 11px 54px;position:relative}
.field::before{content:"";position:absolute;left:14px;top:11px;width:24px;height:24px;background:#9a9a9a}
.login p{font-size:15px;margin:8px 0}
.signin{display:block;margin:6px 0 0 auto;width:140px;height:40px;background:#555;color:#fff;font-size:17px;text-align:center;line-height:40px}
.login-foot{margin-top:36px;display:flex;justify-content:space-between;font-size:16px;color:#fff}
.login-foot span:last-child{color:#9cc8ff}
.categories{margin-top:50px;background:#fff;border:1px solid var(--line)}
.categories h2{background:var(--panel);color:#fff;font-size:30px;font-weight:600;height:60px;line-height:60px;padding-left:22px;position:relative;letter-spacing:1px}
.categories h2::after{content:"";position:absolute;right:30px;top:22px;border:14px solid transparent;border-top-color:#fff}
.categories li{list-style:none;height:52px;border-bottom:1px solid var(--line);font-size:28px;color:#444;padding-left:64px;line-height:50px;position:relative}
.categories li::before{content:"";position:absolute;left:22px;top:16px;border:10px solid transparent;border-left:16px solid #999}
.promo{margin-top:50px;text-align:center}
.promo-photo{width:300px;height:200px;margin:0 auto}
.promo h4{color:var(--orange);font-size:32px;font-weight:400;margin:22px 0 8px}
.promo p{font-size:20px;line-height:1.4;color:#444;padding:0 22px;text-align:left}
.promo.boxed{border:2px solid var(--line);background:#fff;padding:14px 0 20px;margin-top:30px}
.cards{position:absolute;left:448px;top:728px;width:704px}
.card{height:232px;display:flex;margin-bottom:0;border-bottom:4px solid #f4f4f4}
.card-photo{width:246px;flex:none}
.card-body{flex:1;background:var(--card);padding:14px 18px;position:relative}
.card-body h5{color:var(--orange);font-size:18px;font-weight:600;margin-bottom:6px}
.card-body p{font-size:17px;line-height:1.35;color:#333}
.more{position:absolute;right:18px;bottom:14px;background:var(--orange);color:#fff;font-size:15px;font-weight:600;padding:5px 16px}
.footer{position:absolute;left:0;top:3812px;width:1200px;height:268px;background:var(--dark);color:#ccc}
.footer h6{font-size:22px;font-weight:600;color:#fff;margin-bottom:16px}
.fcol{position:absolute;top:30px}
.fcol li{list-style:none;font-size:15px;margin-bottom:9px;color:#aaa}
.fcol li::before{content:"› ";color:var(--orange)}
.sub-field{width:210px;height:36px;background:#1e5aa8;color:#dde;font-size:14px;padding:8px 12px;margin-bottom:10px}
.sub-btn{width:110px;height:34px;background:var(--orange);color:#fff;font-size:14px;text-align:center;line-height:34px}
.social{display:flex;gap:12px}
.social span{width:40px;height:40px;display:block}
.copyright{position:absolute;left:0;top:4080px;width:1200px;height:56px;background:var(--darker);color:#eee;font-size:20px;text-align:center;line-height:56px}
</style>
</head>
<body>
<header class="header">
  <div class="brand"><span class="brand-mark"></span><span class="brand-name">Harbor Institute of Business and Technology</span></div>
  <div class="user-links"><span>Login</span><span>Register</span></div>
  <div class="search"><div class="search-field">search here</div><div class="search-btn"></div></div>
</header>
<nav class="nav">
  <a class="active">Home</a><a>About Us</a><a>Academics</a><a>Admissions</a><a>Mission</a><a>Courses</a><a>Contact Us</a>
</nav>
<div class="hero" role="img" aria-label="Students working at computers in a training lab"></div>

<aside class="sidebar">
  <div class="login">
    <h3>Log in with username &amp; password</h3>
    <div class="field">Username</div>
    <div class="field">Password</div>
    <p>Forgot Your Password?</p>
    <p>☐ Remember me</p>
    <span class="signin">Sign in</span>
    <div class="login-foot"><span>Don't have account?</span><span>Enter new account</span></div>
  </div>
  <div class="categories">
    <h2>CATAGORIES</h2>
    <ul>
      <li>Coaching</li><li>Communicate</li><li>Training</li><li>Requirement</li><li>Reference</li><li>Description</li><li>Website design</li><li>Helping</li>
      <li>Communicate</li><li>Training</li><li>Requirement</li><li>Reference</li><li>Description</li><li>Website design</li><li>Helping</li>
      <li>Communicate</li><li>Training</li><li>Requirement</li><li>Reference</li><li>Description</li><li>Website design</li><li>Helping</li>
    </ul>
  </div>
  <div class="promo">
    <div class="promo-photo" role="img" aria-label="Student using a tablet" style="background:linear-gradient(135deg,#8fb4d4,#3f6f9a)"></div>
    <h4>Description</h4>
    <p>Tried and Tested Robust Versatile Testing Platform - assess Domain skills, IT skills, Cognitive Skills and Language Skills. Customized Assessment - prepared by industry experts. Online Performance and Progress report. Successfully run for large organizations and students.</p>
  </div>
  <div class="promo">
    <div class="promo-photo" role="img" aria-label="Globe beside a laptop" style="background:linear-gradient(135deg,#e8e8e8,#6fa0c8)"></div>
  </div>
  <div class="promo boxed">
    <h4 style="margin-top:6px">Description</h4>
    <p>Tried and Tested Robust Versatile Testing Platform - assess Domain skills, IT skills, Cognitive Skills and Language Skills. Customized Assessment - prepared by industry experts. Online Performance and Progress report. Successfully run for large organizations and students.</p>
  </div>
</aside>

<section class="cards">
  <article class="card"><div class="card-photo" role="img" aria-label="Hand touching a digital interface" style="background:linear-gradient(135deg,#e6f1fa,#5d9ccc)"></div><div class="card-body"><h5>Training and Supporting Software</h5><p>To support this goal, we will improve each stage of the experience ... significant change with the rise of ad blocking software and growing concerns that expanded testing capabilities, and offered.</p><span class="more">Read more</span></div></article>
  <article class="card"><div class="card-photo" role="img" aria-label="Glowing digital network graphic" style="background:linear-gradient(135deg,#0c1a33,#3a7fc0)"></div><div class="card-body"><h5>Training and Supporting Software</h5><p>Bachelor of Science in Information Technology (BSc IT) Bachelor of Computer Applications (BCA) Bachelor of Business Administration (BBA) Bachelor of Commerce in Information System (BCom IS)</p><span class="more">Read more</span></div></article>
  <article class="card"><div class="card-photo" role="img" aria-label="Business professional with technology graphics" style="background:linear-gradient(135deg,#cfe0ee,#6c8fae)"></div><div class="card-body"><h5>Training and Supporting Software</h5><p>Master of Computer Application (MCA) Master of Science in Information Technology (MSIT) Master of Computer Application (MCA) Master of Science in Information Technology (MSIT) Master in Business</p><span class="more">Read more</span></div></article>
  <article class="card"><div class="card-photo" role="img" aria-label="Hand pointing at a touch screen" style="background:linear-gradient(135deg,#1a4a7a,#7fb6e0)"></div><div class="card-body"><h5>Training and Supporting Software</h5><p>PG Diploma in Computer Application (PGDCA) PG Diploma in Computer Application (PGDCA) PG Diploma in Telecommunication and Networking (PGDBA)</p><span class="more">Read more</span></div></article>
  <article class="card"><div class="card-photo" role="img" aria-label="Smartphone surrounded by app icons" style="background:linear-gradient(135deg,#2c5f96,#e2a84a)"></div><div class="card-body"><h5>Training and Supporting Software</h5><p>Bachelor of Science in Information Technology (BSc IT) Bachelor of Computer Applications (BCA) Bachelor of Business Administration (BBA) Bachelor of Commerce in Information System (BCom IS)</p><span class="more">Read more</span></div></article>
  <article class="card"><div class="card-photo" role="img" aria-label="Figure standing on a mountain under clouds" style="background:linear-gradient(180deg,#b8cde0,#4b5f74)"></div><div class="card-body"><h5>Training and Supporting Software</h5><p>To support this goal, we will improve each stage of the experience ... significant change with the rise of ad blocking software and growing concerns that expanded testing capabilities, and offered.</p><span class="more">Read more</span></div></article>
  <article class="card"><div class="card-photo" role="img" aria-label="Server racks in a data centre" style="background:linear-gradient(90deg,#222,#8a8f96,#222)"></div><div class="card-body"><h5>Training and Supporting Software</h5><p>Bachelor of Science in Information Technology (BSc IT) Bachelor of Computer Applications (BCA) Bachelor of Business Administration (BBA) Bachelor of Commerce in Information System (BCom IS)</p><span class="more">Read more</span></div></article>
  <article class="card"><div class="card-photo" role="img" aria-label="Globe beside server hardware" style="background:linear-gradient(135deg,#0a2a5a,#4a90d0)"></div><div class="card-body"><h5>Training and Supporting Software</h5><p>Bachelor of Science in Information Technology (BSc IT) Bachelor of Computer Applications (BCA) Bachelor of Business Administration (BBA) Bachelor of Commerce in Information System (BCom IS)</p><span class="more">Read more</span></div></article>
  <article class="card"><div class="card-photo" role="img" aria-label="Blue technology background" style="background:linear-gradient(135deg,#0f3566,#3b80c4)"></div><div class="card-body"><h5>Training and Supporting Software</h5><p>Bachelor of Science in Information Technology (BSc IT) Bachelor of Computer Applications (BCA) Bachelor of Business Administration (BBA) Bachelor of Commerce in Information System (BCom IS)</p><span class="more">Read more</span></div></article>
  <article class="card"><div class="card-photo" role="img" aria-label="Technician repairing a computer" style="background:linear-gradient(135deg,#d8dde2,#6f8294)"></div><div class="card-body"><h5>Training and Supporting Software</h5><p>Bachelor of Science in Information Technology (BSc IT) Bachelor of Computer Applications (BCA) Bachelor of Business Administration (BBA) Bachelor of Commerce in Information System (BCom IS)</p><span class="more">Read more</span></div></article>
  <article class="card"><div class="card-photo" role="img" aria-label="Support agent wearing a headset" style="background:linear-gradient(135deg,#eef2f5,#8fa3b4)"></div><div class="card-body"><h5>Training and Supporting Software</h5><p>Bachelor of Science in Information Technology (BSc IT) Bachelor of Computer Applications (BCA) Bachelor of Business Administration (BBA) Bachelor of Commerce in Information System (BCom IS)</p><span class="more">Read more</span></div></article>
  <article class="card"><div class="card-photo" role="img" aria-label="Group of business people" style="background:linear-gradient(135deg,#f2f2f2,#5a6470)"></div><div class="card-body"><h5>Training and Supporting Software</h5><p>Bachelor of Science in Information Technology (BSc IT) Bachelor of Computer Applications (BCA) Bachelor of Business Administration (BBA) Bachelor of Commerce in Information System (BCom IS)</p><span class="more">Read more</span></div></article>
  <article class="card"><div class="card-photo" role="img" aria-label="Hand reaching toward a screen" style="background:linear-gradient(135deg,#e8f0f7,#4f86b8)"></div><div class="card-body"><h5>Training and Supporting Software</h5><p>Bachelor of Science in Information Technology (BSc IT) Bachelor of Computer Applications (BCA) Bachelor of Business Administration (BBA) Bachelor of Commerce in Information System (BCom IS)</p><span class="more">Read more</span></div></article>
</section>

<footer class="footer">
  <div class="fcol" style="left:96px"><h6>About Us</h6><ul><li>Our History</li><li>Our Faculty</li><li>Campus Life</li><li>Student News</li><li>Careers</li></ul></div>
  <div class="fcol" style="left:370px"><h6>Services</h6><ul><li>Computer Courses</li><li>Business Courses</li><li>Job Training</li><li>Career Advice</li><li>Free Resources</li></ul></div>
  <div class="fcol" style="left:620px"><h6>Signin</h6><div class="sub-field">Email address</div><div class="sub-field">Password</div><div class="sub-btn">Subscribe now</div></div>
  <div class="fcol" style="left:900px"><h6>Follow Us</h6><div class="social"><span style="background:#3aa8e0"></span><span style="background:#d9382e"></span><span style="background:#3b5a9a"></span><span style="background:#1e6fb0"></span></div></div>
</footer>
<div class="copyright">Copyright@2015, All right Reserved</div>
</body>
</html>
```